Guarenteed! - Homepage Website Design - Coding not required- Winner to complete further pages

Hi all,

We're looking at redesigning our current website with a few adjustments to other pages but the main adjustments will be on the homepage which is what this design request is for. Please note : any of these ideas can be changed if you have something particularly different / special in mind etc.

P.S Coding is not required, just a design.

- Our website -

Our website is simply a price comparison website that allows customers to find companies within their area at the best price. The products available are mostly related to the vehicle trade and all refer to vinyl. This includes the likes of vehicle window tint, vehicle colour change vehicle wrap, vehicle signage as well as other cosmetic vinyl modifications. We allow the customer to search for their product within their chosen area and receive a list of companies who supply their product within that area. From here they can compare prices and view further details on the company.

- What we're looking to do -

We're looking first of all to adjust how the website homepage is displayed, this includes adding images and adjusting the colours that are explained below:

First of all, we look to spread out each of the 12 products (which can be seen on the website as it stands) and add an image to each of the products (all being spaced out as shown in our sketch)

We've been told the website looks too busy so we're thinking if we adjust the colours to more simplier neutral colours as well as the main focus of the website being on the 12 images, that would be great.

- Logo + Banner -

Logo to remain top left although banner may be removed / adjusted to make simplier.

- Colours -

Adjustments - Colours shades
We want the website to still look exciting but simplify the colours. Needs to be kept up to date with the colours / textures etc (bright colours to highlight keypoints)
We're still looking to use either blue or orange or maybe both to highlight these keypoints but the main website to be light colours and maybe even black on white background. The entire homepage can be adjusted colour wise if you feel it fits into your theme including menu bars, banners etc. The key is to get this right with being not too overpowering with the colours but still look interesting and up to date.

- 1 - 4 steps banner - (text may change)

This sits just under the logo and explains to the user how easy the website is to use and the steps they need to take. This may change to a 1 - 5 steps but we're looking to have this designed once the overall colours / theme of the website is sorted.

- 12 images - 4 x 3

This is the main focus of the website and will be the main focus of what the customer sees first of all. This will be where they select their product and then underneath, enter their postcode and distance they would like to search within. As explained further up, we have some of the product images available so if you can where possible add these to the design and then duplicate the images on those we currently don't have available.

- 12 Images -Titles -

These titles will be in this order from left to right and etc

- Colour Change Wrap
- Printed Vehicle Wrap
- Window Tint
- Headlight Tint
- Vehicle Signage
- Shop Signage
- Roof Vinyl Wrap
- Bonnet Vinyl Wrap
- Carbon Fibre Vinyl
- Stickerbomb Vinyl
- Clear Protective Vinyl
- Wheel Refurb

Text to be quite large, centered and with the o to the left of the title. Short titles like 'Window Tint' should fit on one line in the middle of the box where as titles such as ' Stickerbomb Vinyl Wrap' should have the 'Stickerbomb Vinyl' on the first line with the 'Wrap' on the line below. The background of this text is up to experient, might be worth just a simple colour or it might be worth using a bright blue or orange to keep in with the theme of the logo etc.

These will also have the circle tick box to the left of the title (as on the current website) where the customer clicks to select the product they have available.
We were also thinking that if when the customer ticks the circle on their selected box, the box is highlighted in some way to show this.

- Search Block -

This will appear under the 12 images and allows the customer to input their postcode and distance for the search criteria. Colours on this can of course be adjusted to keep in theme with the website.

- Under the 12 Images -

- Block underneath the 12 images and search block -

To the left will be some key bullet points about the website - maybe 4 or 5 with a green tick to the left of this. Background colour will probably be best to be a light colour, possibly grey.

Then to the right of this will appear 4 images, 2 before and 2 after when applying these products. Images to be used aren't fully decided on and we would like this stage of the design left to the end when the rest of the theme etc have been decided on.

Attached images are as follows :
- How the website looks as it stands
- The fold line on the website (obviously important)
- Our rough sketch of how we'd like the website homepage to look.
- We have 7 of the images ready that are all attached in this one file. Please duplicate the images on those that currently don't have the image available.

We will also be requesting a website developer to put this into action if our current designer falls through so please feel free to contact us if potentially interested.

The layout can change if you can think of something particular different / unique that works with this design. The main idea is to not only get the 12 products on view to the viewers but also the keypoints and before and after images.

Any questions, please ask away as we're bound to have forgotten a few things.

Thanks and good luck!

Hi all, keep the designs coming.

We haven't quite seen that extra special design we're after. As stated, we're after something fairly simple to suit the youth as well as the middle aged but we're also after something that bit special.

Colours to concentrate on are still and orange etc although feel free to use other colours if you have anything special in mind.

Please experience and we'll give you our honest feedback.

Many thanks all and good luck!

Hi all, this is a message to all the designers.

Some good designs coming in but we're still after that something special for the website design. Keep the designs coming and please feel free to experiment with the design colours, layout etc.

The basic principle of the website needs to remain regarding the 12 products, search within block and 4 steps all appearing on the homepage.

The 4 steps seems to work best when it's got text as well as some simple images next to this.

A variation with the product titles with how to display this, some designers have gone with a simple white background whereas others have gone with colours. Please experiment here and where possible, add a contract / texture to the colour. Please remember the product titles needs to be clear, centured and with the circle tick box to the left of it. 

We're after a fairly simple design although we need it to look 21st century, up to date as well as interesting. The key points straight away are the 4 steps as well as the 12 products so try to guide the viewer to these areas a little.

White background behind the 12 images seems to be a much, although a light colour could possibly work.

The keypoints underneath these 12 products are too very important as it outlines what we do etc. Tick colour can vary.

Next to these keypoints will be the 'before' and 'after' images, these images needs to be fairly small and ensure there is white background around the image itself.

Good luck all and any questions, feel free to ask away.

Thanks!

Hi,

 Thank you for your time and effort with these designs, we are very nearly there with the design but we've thought of something that may work for the homepage. A curved arrow from step 1 pointing to the products, this may or may not work but feel free to give it a go.

Many thanks,

Thank you to everyone for your time and efforts with the design. It's hugely appreciated so thank you all once again.

Wish you all the luck in the future.

```html
<!DOCTYPE html>
<html lang="en">
<head>
<meta charset="utf-8">
<title>WrapLocate Pro – Find and Compare Vinyl Installers</title>
<link href="https://fonts.googleapis.com/css2?family=Roboto:wght@300;400;500;700&display=swap" rel="stylesheet">
<style>
:root{
  --navy:#34477a;
  --navy-dark:#2b3b66;
  --orange:#ee7021;
  --orange-dark:#d45f15;
  --grey-band:#e1e1e1;
  --grey-panel:#ececec;
  --grey-box:#e2e2e2;
  --text:#3d3d3d;
  --muted:#8a8a8a;
  --tick:#3bb54a;
  --white:#ffffff;
}
*{box-sizing:border-box;margin:0;padding:0}
html,body{width:1087px;height:1200px;overflow:hidden}
body{position:relative;font-family:"Roboto",Arial,sans-serif;font-weight:300;color:var(--text);background:var(--white)}
.abs{position:absolute}

.top-rule{left:0;top:0;width:1087px;height:3px;background:var(--navy)}
.site-header{left:0;top:3px;width:1087px;height:88px;background:linear-gradient(#f6f6f6,#ffffff)}
.brand{left:0;top:22px;width:1087px;text-align:center;display:flex;justify-content:center;align-items:center;gap:8px}
.brand-dot{width:14px;height:14px;border-radius:50%;background:var(--orange)}
.brand-name{font-weight:500;font-size:17px;color:var(--navy);letter-spacing:1px}
.brand-tag{left:0;top:45px;width:1087px;text-align:center;font-size:7px;color:var(--navy);font-weight:500;letter-spacing:.5px}

.steps-band{left:0;top:91px;width:1087px;height:125px;background:var(--grey-band);border-top:1px solid #cfcfcf}
.main-nav{left:255px;top:76px;width:576px;height:30px}
.main-nav svg{position:absolute;left:0;top:0}
.nav-links{position:absolute;left:28px;top:0;height:30px;display:flex;align-items:center;gap:22px;font-size:9px;font-weight:400}
.nav-links a{color:#8ea0d1;text-decoration:none}
.nav-links a.current{color:var(--white)}
.nav-cta{position:absolute;left:434px;top:0;height:30px;display:flex;align-items:center;font-size:9px;font-weight:400;color:var(--white)}

.how-note{left:190px;top:138px;font-size:10px;color:#777;transform:rotate(-28deg);transform-origin:left top;line-height:10px}
.step{width:130px;text-align:center;top:124px}
.step-ring{width:42px;height:42px;margin:0 auto;border-radius:50%;border:1px solid #b8b8b8;display:flex;align-items:center;justify-content:center}
.step-num{width:36px;height:36px;border-radius:50%;border:1px solid #9a9a9a;background:#f2f2f2;display:flex;align-items:center;justify-content:center;font-size:16px;color:var(--navy)}
.step-label{margin-top:7px;font-size:11.5px;line-height:12px;color:#555}
.step-line{top:144px;height:1px;background:#b5b5b5}

.product{width:131px;height:147px;background:var(--white);box-shadow:0 2px 3px rgba(0,0,0,.22);border:1px solid #d3d3d3}
.product .photo{height:95px;width:100%}
.product .title{position:absolute;left:0;bottom:0;width:100%;height:50px;background:var(--navy);color:var(--white);font-size:12px;line-height:12px;display:flex;align-items:center;justify-content:center;text-align:center;font-weight:300}
.product.selected{border-color:var(--orange)}
.product.selected .title{background:var(--orange);font-weight:700}
.check{position:absolute;right:7px;top:6px;width:16px;height:16px;border-radius:50%;background:var(--white);border:1px solid #777}
.product.selected .check{background:var(--orange);border-color:var(--orange)}
.check svg{position:absolute;left:3px;top:4px}

.search-bar{left:255px;top:727px;width:576px;height:51px;background:#d9d9d9;box-shadow:0 2px 0 #bdbdbd}
.search-label{left:28px;top:17px;font-size:14px;color:#777;font-weight:500}
.search-label span{font-weight:300}
.field{top:12px;height:27px;background:#f1f1f1;border-radius:2px;box-shadow:inset 0 1px 2px rgba(0,0,0,.15);font-size:14px;color:#555}
.field .val{position:absolute;left:13px;top:5px}
.field .sep{position:absolute;top:3px;width:1px;height:21px;background:#d8d8d8}
.field .unit{position:absolute;top:8px;font-size:9px;color:#bbb;font-weight:400}
.of{left:288px;top:17px;font-size:14px;color:#888}
.search-btn{left:453px;top:12px}
.search-btn span{position:absolute;left:20px;top:7px;color:var(--white);font-size:11px;font-weight:400}

.lower{left:0;top:816px;width:1087px;height:384px;background:var(--grey-band);border-top:1px solid #cfcfcf}
.features{left:255px;top:813px;width:204px;height:332px;background:var(--grey-panel);box-shadow:2px 2px 3px rgba(0,0,0,.25)}
.features h2{position:absolute;left:22px;top:21px;font-size:20px;font-weight:300;color:var(--navy)}
.features .rule{position:absolute;left:22px;top:52px;width:170px;height:1px;background:#c7c7c7}
.features ul{position:absolute;left:22px;top:72px;width:170px;list-style:none}
.features li{position:relative;padding-left:17px;font-size:7.5px;line-height:11px;color:#444;font-weight:400;margin-bottom:12px}
.features li svg{position:absolute;left:0;top:1px}
.features-foot{position:absolute;left:0;bottom:0;width:204px;height:79px;background:var(--orange)}
.mail-btn{position:absolute;left:11px;top:10px;width:181px;height:28px;border:2px solid #fbd2b5;color:var(--white);font-size:10px;font-weight:400;display:flex;align-items:center;justify-content:center}
.copyright{position:absolute;left:0;top:51px;width:100%;text-align:center;color:var(--white);font-size:9px;font-weight:400}

.ba-head{top:835px;font-size:20px;color:var(--navy)}
.ba-rule{left:481px;top:865px;width:350px;height:1px;background:#c7c7c7}
.ba-frame{width:158px;height:121px;background:var(--grey-box);border:3px solid var(--white);box-shadow:0 1px 3px rgba(0,0,0,.3)}
</style>
</head>
<body>

<div class="abs top-rule"></div>
<header class="abs site-header"></header>
<div class="abs brand"><span class="brand-dot"></span><span class="brand-name">WRAPLOCATE PRO</span></div>
<div class="abs brand-tag">Find and Compare Vinyl Installers</div>

<section class="abs steps-band"></section>

<nav class="abs main-nav">
  <svg width="576" height="30" viewBox="0 0 576 30">
    <polygon points="0,0 413,0 413,30 0,30 6,15" fill="var(--navy)"/>
    <polygon points="413,0 576,0 570,15 576,30 413,30" fill="var(--orange)"/>
    <polyline points="550,10 554,15 550,20" fill="none" stroke="#fff" stroke-width="1.3"/>
  </svg>
  <div class="nav-links">
    <a class="current">HOME</a><a>ABOUT US</a><a>CONTACT US</a><a>BLOG</a>
  </div>
  <div class="nav-cta">LIST YOUR COMPANY HERE</div>
</nav>

<div class="abs how-note">How does<br>&nbsp;&nbsp;it work?</div>
<svg class="abs" style="left:215px;top:150px" width="36" height="34" viewBox="0 0 36 34">
  <path d="M4 2 C2 16 14 28 31 29" fill="none" stroke="#777" stroke-width="1.3"/>
  <polyline points="25,24 31,29 25,33" fill="none" stroke="#777" stroke-width="1.3"/>
</svg>

<div class="abs step-line" style="left:344px;width:104px"></div>
<div class="abs step-line" style="left:491px;width:104px"></div>
<div class="abs step-line" style="left:639px;width:104px"></div>

<div class="abs step" style="left:257px"><div class="step-ring"><div class="step-num">1</div></div><div class="step-label">Select Chosen<br>Product</div></div>
<div class="abs step" style="left:404px"><div class="step-ring"><div class="step-num">2</div></div><div class="step-label">Input Postcode,<br>Distance + Search</div></div>
<div class="abs step" style="left:552px"><div class="step-ring"><div class="step-num">3</div></div><div class="step-label">Compare Companies<br>&amp; Prices</div></div>
<div class="abs step" style="left:699px"><div class="step-ring"><div class="step-num">4</div></div><div class="step-label">Contact Chosen<br>Company</div></div>

<!-- product grid -->
<div class="abs product" style="left:266px;top:234px"><div class="photo" role="img" aria-label="Photo of a green and a red hatchback car" style="background:linear-gradient(135deg,#e9efe9,#8fbf7a 50%,#d86a6a)"></div><div class="check"><svg width="9" height="7" viewBox="0 0 9 7"><polyline points="1,3.5 3.5,6 8,1" fill="none" stroke="#333" stroke-width="1.3"/></svg></div><div class="title">COLOUR CHANGE<br>WRAP</div></div>
<div class="abs product" style="left:408px;top:234px"><div class="photo" role="img" aria-label="Photo of a van with a printed wrap" style="background:linear-gradient(180deg,#b9cde6,#eef0f0 55%,#6e9a55)"></div><div class="check"><svg width="9" height="7" viewBox="0 0 9 7"><polyline points="1,3.5 3.5,6 8,1" fill="none" stroke="#333" stroke-width="1.3"/></svg></div><div class="title">PRINTED VEHICLE<br>WRAP</div></div>
<div class="abs product" style="left:550px;top:234px"><div class="photo" role="img" aria-label="Photo of two green cars with tinted windows" style="background:linear-gradient(135deg,#eef2ee,#7fc06a 55%,#f3f3f3)"></div><div class="check"><svg width="9" height="7" viewBox="0 0 9 7"><polyline points="1,3.5 3.5,6 8,1" fill="none" stroke="#333" stroke-width="1.3"/></svg></div><div class="title">WINDOW<br>TINT</div></div>
<div class="abs product selected" style="left:691px;top:234px"><div class="photo" role="img" aria-label="Photo of a silver car front with tinted headlights" style="background:linear-gradient(160deg,#c9c9c9,#9a9a9a 60%,#e6e6e6)"></div><div class="check"><svg width="9" height="7" viewBox="0 0 9 7"><polyline points="1,3.5 3.5,6 8,1" fill="none" stroke="#333" stroke-width="1.3"/></svg></div><div class="title">HEADLIGHT<br>TINT</div></div>

<div class="abs product" style="left:266px;top:398px"><div class="photo" role="img" aria-label="Photo of a white van with lettered signage" style="background:linear-gradient(180deg,#f6f6f6,#dcdcdc 70%,#f4f4f4)"></div><div class="check"><svg width="9" height="7" viewBox="0 0 9 7"><polyline points="1,3.5 3.5,6 8,1" fill="none" stroke="#333" stroke-width="1.3"/></svg></div><div class="title">VEHICLE<br>SIGNAGE</div></div>
<div class="abs product" style="left:408px;top:398px"><div class="photo" role="img" aria-label="Photo of a shop front with a window sign" style="background:linear-gradient(180deg,#d8d8d8,#5a5f66 45%,#c9c9c9)"></div><div class="check"><svg width="9" height="7" viewBox="0 0 9 7"><polyline points="1,3.5 3.5,6 8,1" fill="none" stroke="#333" stroke-width="1.3"/></svg></div><div class="title">SHOP<br>SIGNAGE</div></div>
<div class="abs product selected" style="left:550px;top:398px"><div class="photo" role="img" aria-label="Photo of a silver car with a black vinyl roof" style="background:radial-gradient(circle at 50% 45%,#555 0 18%,#b5b5b5 35%,#f4f4f4 60%)"></div><div class="check"><svg width="9" height="7" viewBox="0 0 9 7"><polyline points="1,3.5 3.5,6 8,1" fill="none" stroke="#333" stroke-width="1.3"/></svg></div><div class="title">ROOF VINYL<br>WRAP</div></div>
<div class="abs product" style="left:691px;top:398px"><div class="photo" role="img" aria-label="Photo of a silver car with a black vinyl bonnet" style="background:radial-gradient(circle at 45% 55%,#555 0 16%,#b5b5b5 34%,#f4f4f4 60%)"></div><div class="check"><svg width="9" height="7" viewBox="0 0 9 7"><polyline points="1,3.5 3.5,6 8,1" fill="none" stroke="#333" stroke-width="1.3"/></svg></div><div class="title">BONNET VINYL<br>WRAP</div></div>

<div class="abs product" style="left:266px;top:562px"><div class="photo" role="img" aria-label="Photo of a roll of carbon fibre vinyl" style="background:linear-gradient(135deg,#f2f2f2 20%,#2a2a2a 45%,#111)"></div><div class="check"><svg width="9" height="7" viewBox="0 0 9 7"><polyline points="1,3.5 3.5,6 8,1" fill="none" stroke="#333" stroke-width="1.3"/></svg></div><div class="title">CARBON FIBER<br>VINYL</div></div>
<div class="abs product" style="left:408px;top:562px"><div class="photo" role="img" aria-label="Photo of a white car with a stickerbomb bonnet" style="background:linear-gradient(180deg,#f2f2f2,#e3b24d 40%,#d9d9d9 75%)"></div><div class="check"><svg width="9" height="7" viewBox="0 0 9 7"><polyline points="1,3.5 3.5,6 8,1" fill="none" stroke="#333" stroke-width="1.3"/></svg></div><div class="title">STICKERBOMB<br>VINYL</div></div>
<div class="abs product" style="left:550px;top:562px"><div class="photo" role="img" aria-label="Photo of a silver car with clear protective film" style="background:radial-gradient(circle at 50% 45%,#666 0 14%,#b5b5b5 34%,#f4f4f4 60%)"></div><div class="check"><svg width="9" height="7" viewBox="0 0 9 7"><polyline points="1,3.5 3.5,6 8,1" fill="none" stroke="#333" stroke-width="1.3"/></svg></div><div class="title">CLEAR PROTECTIVE<br>VINYL</div></div>
<div class="abs product" style="left:691px;top:562px"><div class="photo" role="img" aria-label="Photo of a damaged and a refurbished alloy wheel" style="background:linear-gradient(90deg,#6b6560,#a29d98 50%,#7c7c80)"></div><div class="title">WHEEL<br>REFURB</div></div>

<!-- search -->
<section class="abs search-bar">
  <div class="abs search-label">SEARCH <span>WITHIN:</span></div>
  <div class="abs field" style="left:147px;width:130px"><span class="val">10</span><span class="sep" style="left:65px"></span><span class="unit" style="left:77px">⊙ MILES</span></div>
  <div class="abs of">OF</div>
  <div class="abs field" style="left:317px;width:118px"><span class="val">90210</span><span class="sep" style="left:65px"></span><span class="unit" style="left:76px">ZIP</span></div>
  <div class="abs search-btn">
    <svg width="108" height="29" viewBox="0 0 108 29">
      <polygon points="0,0 101,0 108,14.5 101,29 0,29" fill="var(--orange)"/>
      <circle cx="79" cy="13" r="5" fill="none" stroke="#fff" stroke-width="2"/>
      <line x1="82.5" y1="16.5" x2="86.5" y2="20.5" stroke="#fff" stroke-width="2.2"/>
    </svg>
    <span>SEARCH</span>
  </div>
</section>

<!-- lower area -->
<section class="abs lower"></section>

<aside class="abs features">
  <h2>Key Features</h2>
  <div class="rule"></div>
  <ul>
    <li><svg width="11" height="9" viewBox="0 0 11 9"><polyline points="1,4.5 4,7.5 10,1" fill="none" stroke="var(--tick)" stroke-width="1.8"/></svg>Vivamus tincidunt vel nibh accumsan rhoncus.</li>
    <li><svg width="11" height="9" viewBox="0 0 11 9"><polyline points="1,4.5 4,7.5 10,1" fill="none" stroke="var(--tick)" stroke-width="1.8"/></svg>Mauris pretium massa quis urna porttitor tempor.</li>
    <li><svg width="11" height="9" viewBox="0 0 11 9"><polyline points="1,4.5 4,7.5 10,1" fill="none" stroke="var(--tick)" stroke-width="1.8"/></svg>Fusce faucibus metus quam, et vulputate magna condimentum ac.</li>
    <li><svg width="11" height="9" viewBox="0 0 11 9"><polyline points="1,4.5 4,7.5 10,1" fill="none" stroke="var(--tick)" stroke-width="1.8"/></svg>Cras sit amet sodales ipsum. Sed ullamcorper accumsan ultrices.</li>
    <li><svg width="11" height="9" viewBox="0 0 11 9"><polyline points="1,4.5 4,7.5 10,1" fill="none" stroke="var(--tick)" stroke-width="1.8"/></svg>Pellentesque vitae leo vel nulla aliquam pellentesque.</li>
  </ul>
  <div class="features-foot">
    <div class="mail-btn">JOIN OUR MAILING LIST</div>
    <div class="copyright">Copyright 2013 © WrapLocate Pro</div>
  </div>
</aside>

<div class="abs ba-head" style="left:502px">Before:</div>
<div class="abs ba-head" style="left:767px">After:</div>
<div class="abs ba-rule"></div>
<div class="abs ba-frame" role="img" aria-label="Before image placeholder" style="left:493px;top:882px"></div>
<div class="abs ba-frame" role="img" aria-label="After image placeholder" style="left:663px;top:882px"></div>
<div class="abs ba-frame" role="img" aria-label="Before image placeholder" style="left:493px;top:1023px"></div>
<div class="abs ba-frame" role="img" aria-label="After image placeholder" style="left:663px;top:1023px"></div>

</body>
</html>
```